Harbor Petroleum Business Cards

I would like to design some options for about 10 sets of double sided business cards for our team with a raised logo with a Silver glossy finished logo. We are a privately funded upstream Oil & Gas producer drilling vertical wells in Central Oklahoma with a long term production (ROI driven) strategy that we implement through an annual drilling program. We are focused on a shallow / vertical / long life / low decline strategy. We are based in downtown Tulsa Oklahoma. I have attached a sample business card and a picture of our hallway logo which we would like to replicate on the business cards.

Target Market(s)

SEC Accredited Investors and other Oil & Gas Operators

Industry/Entity Type

Upstream Oil & Gas

Contact Information for Business Card

You can see the sample photo attached, but email / website / address / direct phone / Cell Phone / Name / Title / Fax

Font styles to use
Other font styles liked:
• Felix Titling

Colors
0054AA
0677BA
7BADD7
CADEEF
E8F1F8

Requirements
Must have
• Glossy raised logo
Nice to have
• Possibly a new logo.
Should not have
• No Greens /

```html
<!DOCTYPE html>
<html lang="en">
<head>
<meta charset="utf-8">
<title>Harbor Petroleum Business Cards</title>
<link href="https://fonts.googleapis.com/css2?family=Tinos:ital,wght@0,400;1,700&display=swap" rel="stylesheet">
<style>
  :root {
    --stage: #e4e4e4;
    --card: #ffffff;
    --panel: #55524e;
    --panel-text: #ffffff;
    --brand-ink: #3f3c39;
    --silver: #b9b9b9;
  }
  * { margin: 0; padding: 0; box-sizing: border-box; }
  html, body { width: 1200px; height: 1200px; overflow: hidden; }
  body {
    background: var(--stage);
    font-family: "Tinos", "Times New Roman", serif;
    position: relative;
  }
  .card {
    position: absolute;
    left: 172px;
    width: 856px;
    height: 501px;
    background: var(--card);
    overflow: hidden;
  }
  .card--front { top: 82px; }
  .card--back { top: 615px; }

  .panel { position: absolute; inset: 0; width: 100%; height: 100%; }
  .panel path { fill: var(--panel); }

  .brand {
    position: absolute;
    display: flex;
    flex-direction: column;
    align-items: center;
    gap: 14px;
    transform: translate(-50%, -50%);
  }
  .brand__dot {
    width: 22px; height: 22px; border-radius: 50%;
    background: var(--silver);
  }
  .brand__name {
    font-size: 25px;
    font-weight: 400;
    letter-spacing: 0.5px;
    text-transform: uppercase;
    color: var(--brand-ink);
    white-space: nowrap;
  }
  .card--front .brand { left: 214px; top: 300px; }
  .card--back .brand { left: 589px; top: 400px; }
  .card--back .brand__name { font-size: 27px; }

  .identity {
    position: absolute;
    right: 50px;
    text-align: right;
    color: var(--panel-text);
  }
  .identity__name { top: 72px; font-size: 28px; font-weight: 400; }
  .identity__title {
    top: 122px;
    font-size: 18px;
    font-style: italic;
    font-weight: 700;
    line-height: 27px;
  }

  .contact {
    position: absolute;
    right: 44px;
    display: flex;
    align-items: center;
    gap: 14px;
    font-size: 18px;
    color: var(--panel-text);
    height: 24px;
    white-space: nowrap;
  }
  .contact svg { width: 14px; height: 14px; fill: var(--panel-text); flex: none; }
  .contact--direct { top: 229px; }
  .contact--cell { top: 265px; }
  .contact--fax { top: 302px; }
  .contact--email { top: 357px; }
  .contact--web { top: 393px; }
  .contact--address { top: 428px; }
</style>
</head>
<body>
  <section class="card card--front" aria-label="Business card front">
    <svg class="panel" viewBox="0 0 685 400" preserveAspectRatio="none" aria-hidden="true">
      <path d="M224 0 C224 110 300 171 412 171 L412 264 C300 264 224 300 224 400 L685 400 L685 0 Z"/>
    </svg>

    <div class="brand">
      <span class="brand__dot"></span>
      <span class="brand__name">Harbor Petroleum, LLC</span>
    </div>

    <h1 class="identity identity__name">Dalton R. Whitcombe, CPL</h1>
    <p class="identity identity__title">Executive Vice President<br>Land, Legal &amp; Business Development</p>

    <p class="contact contact--direct">555-201-4478
      <svg viewBox="0 0 16 16"><path d="M3.5 1.5l2.5 0 1 3.5-1.6 1.2c.8 1.8 2.2 3.2 4 4l1.2-1.6 3.4 1V12c0 1.4-1.2 2.5-2.6 2.4C6 14 2 10 1.6 4.1 1.5 2.7 2.2 1.5 3.5 1.5z"/></svg>
    </p>
    <p class="contact contact--cell">555-318-6620
      <svg viewBox="0 0 16 16"><path d="M4.5 0.5h7a1 1 0 0 1 1 1v13a1 1 0 0 1-1 1h-7a1 1 0 0 1-1-1v-13a1 1 0 0 1 1-1zm.5 2v10h6v-10zm3 11a.8.8 0 1 0 0 .01z"/></svg>
    </p>
    <p class="contact contact--fax">555-402-9135
      <svg viewBox="0 0 16 16"><path d="M4 1h8v4H4zM1.5 6h13a1 1 0 0 1 1 1v5h-3v3h-9v-3h-3V7a1 1 0 0 1 1-1zm3.5 5v2.5h6V11z"/></svg>
    </p>
    <p class="contact contact--email">DRW@HPTulsa.com
      <svg viewBox="0 0 16 16"><path d="M1 3h14v1.2L8 9 1 4.2zM1 6l7 4.8L15 6v7H1z"/></svg>
    </p>
    <p class="contact contact--web">www.HarborPetroleumLLC.com
      <svg viewBox="0 0 16 16"><path d="M8 1a7 7 0 1 0 0 14A7 7 0 0 0 8 1zm0 1.5c.9 1 1.6 2.6 1.8 4.5H6.2C6.4 5.1 7.1 3.5 8 2.5zM2.6 7h2.1c.1 1.6.5 3.1 1.2 4.3A5.5 5.5 0 0 1 2.6 7zm0 1.5zM11.3 7h2.1a5.5 5.5 0 0 1-3.3 4.3c.7-1.2 1.1-2.7 1.2-4.3zM6.2 8.5h3.6c-.2 1.9-.9 3.5-1.8 4.5-.9-1-1.6-2.6-1.8-4.5z"/></svg>
    </p>
    <p class="contact contact--address">220 South Main St., Suite 900 Tulsa, OK 74103
      <svg viewBox="0 0 16 16"><path d="M8 0.5a5 5 0 0 1 5 5c0 3.5-5 8-5 8s-5-4.5-5-8a5 5 0 0 1 5-5zm0 3a2 2 0 1 0 0 4 2 2 0 0 0 0-4zM3 14h10v1.5H3z"/></svg>
    </p>
  </section>

  <section class="card card--back" aria-label="Business card back">
    <div class="brand">
      <span class="brand__dot"></span>
      <span class="brand__name">Harbor Petroleum, LLC</span>
    </div>
  </section>
</body>
</html>
```